Carrying bags for customer visit

I am looking to make a carrying case that can be used to carry small presents, gifts, our brochure (20 inch X20 inch) and sometimes our samples (which are printed circuit boards that have a size of 24X15). The case should look elegant, show our company logo and our slogan "PCB is our business". You can try to download our logo from our web site www.tarnvolt.com. I want a contemporary and cool feel of the carrying case that can be any materials. I prefer to use recyclable materials that reflects our company's business philosophy of practicing sustanbility. Also I would like to add Chinese name “锦泰电路(东莞)有限公司" in the bag.
Updates

Need extra days to review

Target Market(s)

Corporate customers who will come into contact with our companies

Colors

Designer to choose colors to be used in the design.

Requirements
Must have
• It has to be attractive and people wanting to use them on a regular basis. Therefore, the logo display and our slogan should be subtle. I want the carrying bags not to be very expensive to produce.

```html
<!DOCTYPE html>
<html lang="en">
<head>
<meta charset="utf-8">
<title>Tarnvolt Carrying Bag</title>
<link href="https://fonts.googleapis.com/css2?family=Oswald:wght@300&family=Russo+One&family=Noto+Serif+SC:wght@400&family=Roboto:wght@400&display=swap" rel="stylesheet">
<style>
  :root {
    --backdrop: #b9b9b9;
    --paper: #ffffff;
    --brand-green: #0e6a47;
    --ink: #141414;
    --wave-teal: #a9ddd8;
    --wave-light: #e4f4f2;
    --rule-grey: #c9d6d3;
  }
  html, body {
    margin: 0;
    padding: 0;
    width: 1200px;
    height: 834px;
    overflow: hidden;
    background: var(--backdrop);
  }
  .canvas {
    position: relative;
    width: 1200px;
    height: 834px;
  }
  .bag-front {
    position: absolute;
    left: 340px;
    top: 57px;
    width: 520px;
    height: 720px;
    background: var(--paper);
    overflow: hidden;
  }
  .brand {
    position: absolute;
    top: 96px;
    left: 0;
    width: 100%;
    text-align: center;
    font-family: "Russo One", sans-serif;
    font-size: 34px;
    letter-spacing: 2px;
    color: var(--brand-green);
    line-height: 1;
  }
  .slogan {
    position: absolute;
    top: 232px;
    left: 0;
    width: 100%;
    text-align: center;
    line-height: 1;
  }
  .slogan-lead {
    font-family: "Oswald", sans-serif;
    font-weight: 300;
    font-size: 50px;
    color: var(--ink);
    letter-spacing: -1px;
    padding-left: 20px;
  }
  .slogan-key {
    font-family: "Russo One", sans-serif;
    font-size: 48px;
    color: var(--brand-green);
    letter-spacing: 1px;
    margin-top: -6px;
  }
  .wave-area {
    position: absolute;
    left: 0;
    top: 340px;
    width: 520px;
    height: 200px;
    background: linear-gradient(170deg, var(--wave-light) 0%, var(--wave-teal) 30%, var(--wave-light) 60%, var(--paper) 100%);
    opacity: 0.8;
  }
  .company-cn {
    position: absolute;
    top: 556px;
    left: 50px;
    width: 420px;
    text-align: center;
    font-family: "Noto Serif SC", serif;
    font-size: 18px;
    letter-spacing: 2px;
    color: var(--brand-green);
    padding: 10px 0;
    border-top: 1px solid var(--rule-grey);
    border-bottom: 1px solid var(--rule-grey);
  }
  .recycle-note {
    position: absolute;
    top: 640px;
    left: 0;
    width: 100%;
    text-align: center;
    font-family: "Roboto", sans-serif;
    font-size: 12px;
    color: var(--ink);
  }
  .recycle-note svg {
    vertical-align: -2px;
    margin-right: 5px;
  }
</style>
</head>
<body>
<div class="canvas">
  <div class="bag-front">
    <div class="brand">TARNVOLT</div>

    <div class="slogan">
      <div class="slogan-lead">PCB IS OUR</div>
      <div class="slogan-key">BUSINESS</div>
    </div>

    <div class="wave-area" role="img" aria-label="Soft flowing teal line wave decoration"></div>

    <div class="company-cn">锦泰电路(东莞)有限公司</div>

    <div class="recycle-note">
      <svg width="12" height="12" viewBox="0 0 12 12" aria-hidden="true">
        <circle cx="6" cy="6" r="4.5" fill="none" stroke="var(--ink)" stroke-width="1.4"/>
      </svg>Recyclable materials
    </div>
  </div>
</div>
</body>
</html>
```